Mega Fruited Condom Packaging

After the moderately successful relaunch of Voro condoms in a new pack design we would like you to develop eye catching range addition incorporating current pack copy, colours and Voro logo.
This will be available in a pack of 12 condoms and bulk pack 144 with equal quantities of grape, strawberry, orange and apple flavours. These flavours will stand out from what is currently available on the market in that they taste and smell delicious! The name ‘Mega Tasty’ is preferred only since it has synergy with the Mega Slim condom. Also thought about ‘Prime Tasty’ and ‘Mega Fruited’ but open to change if you have a better name
The flavoured condom itself will be the colour of the relevant fruit: Grape-purple, Strawberry-red, Orange-orange and Apple-green.
The range extension should help sell in to adult stores and encourage trial by consumers.
Look and feel
Each slider illustrates characteristics of the customer's brand and the style your logo design should communicate.

```html
<!DOCTYPE html>
<html lang="en">
<head>
<meta charset="utf-8">
<title>Voro Mega Tasty Condoms – Pack Range</title>
<link rel="stylesheet" href="https://fonts.googleapis.com/css2?family=Comfortaa:wght@300;500;700&display=swap">
<style>
  :root {
    --bg: #ece8e3;
    --pack-white: #f7f7f7;
    --navy: #1d2a55;
    --grape: #6b2a7d;
    --grape-soft: #b9a3c4;
    --strawberry: #d42a2a;
    --strawberry-soft: #f0a890;
    --orange: #e35b1c;
    --orange-soft: #f3b08d;
  }
  * { box-sizing: border-box; margin: 0; padding: 0; }
  html, body { width: 1200px; height: 840px; overflow: hidden; }
  body {
    background: var(--bg);
    font-family: "Comfortaa", sans-serif;
  }
  .range {
    position: relative;
    width: 1200px;
    height: 840px;
    display: flex;
    justify-content: center;
    align-items: center;
    gap: 34px;
  }
  .pack {
    position: relative;
    width: 340px;
    height: 620px;
    background: var(--pack-white);
    overflow: hidden;
    box-shadow: 0 6px 18px rgba(0,0,0,.12);
  }
  .pack--grape { --accent: var(--grape); --soft: var(--grape-soft); --fruit-a: #5a2a6e; --fruit-b: #8a5a9e; }
  .pack--strawberry { --accent: var(--strawberry); --soft: var(--strawberry-soft); --fruit-a: #c81e24; --fruit-b: #e85a4a; }
  .pack--orange { --accent: var(--orange); --soft: var(--orange-soft); --fruit-a: #f08a1a; --fruit-b: #f6c060; }

  .pack__top-band {
    position: absolute; top: 0; left: 0; right: 0; height: 14px;
    background: var(--accent);
  }
  .pack__ribbons {
    position: absolute; top: 14px; right: 0; width: 180px; bottom: 0;
    background: linear-gradient(100deg, rgba(255,255,255,0) 0%, var(--soft) 55%, rgba(255,255,255,0) 100%);
    opacity: .55;
  }
  .pack__brand {
    position: absolute; top: 56px; left: 34px;
    display: flex; align-items: center; gap: 10px;
    font-weight: 500; font-size: 40px; color: var(--navy); letter-spacing: 1px;
  }
  .pack__brand-dot {
    width: 14px; height: 14px; border-radius: 50%; background: var(--navy);
  }
  .pack__count {
    position: absolute; top: 42px; right: 26px;
    font-weight: 700; font-size: 62px; color: var(--accent);
  }
  .pack__rule {
    position: absolute; left: 40px; right: 0; height: 2px; background: var(--accent);
  }
  .pack__rule--upper { top: 136px; }
  .pack__rule--lower { top: 226px; }
  .pack__variant {
    position: absolute; top: 144px; left: 52px;
    color: var(--accent); font-size: 25px; line-height: 26px;
  }
  .pack__variant b { font-weight: 700; display: block; }
  .pack__variant span { font-weight: 300; display: block; }
  .pack__claim {
    position: absolute; top: 318px; left: 52px;
    color: var(--accent); font-weight: 700; font-size: 46px; line-height: 42px;
    letter-spacing: -1px;
  }
  .pack__fruit {
    position: absolute; top: 490px; left: 58px; width: 170px; height: 90px;
    border-radius: 40px;
    background: radial-gradient(circle at 40% 40%, var(--fruit-b), var(--fruit-a));
  }
  .pack__flavour {
    position: absolute; bottom: 14px; left: 52px;
    color: var(--accent); font-weight: 300; font-size: 13px; opacity: .8;
  }
  .pack__code {
    position: absolute; bottom: 14px; right: 24px;
    color: var(--accent); font-weight: 300; font-size: 24px; opacity: .5;
  }
</style>
</head>
<body>
<main class="range">
  <article class="pack pack--grape">
    <div class="pack__top-band"></div>
    <div class="pack__ribbons" role="img" aria-label="Translucent purple smoke ribbons"></div>
    <div class="pack__brand"><span class="pack__brand-dot"></span>VORO</div>
    <div class="pack__count">12</div>
    <div class="pack__rule pack__rule--upper"></div>
    <div class="pack__variant"><b>MEGA TASTY</b><b>MEGA SLIM</b><span>CONDOMS</span></div>
    <div class="pack__rule pack__rule--lower"></div>
    <h2 class="pack__claim">SAFE<br>SEX<br>GREAT<br>SEX</h2>
    <div class="pack__fruit" role="img" aria-label="Photo of a bunch of purple grapes"></div>
    <p class="pack__flavour">GRAPE FLAVORED</p>
    <p class="pack__code">53</p>
  </article>

  <article class="pack pack--strawberry">
    <div class="pack__top-band"></div>
    <div class="pack__ribbons" role="img" aria-label="Translucent coral smoke ribbons"></div>
    <div class="pack__brand"><span class="pack__brand-dot"></span>VORO</div>
    <div class="pack__count">12</div>
    <div class="pack__rule pack__rule--upper"></div>
    <div class="pack__variant"><b>MEGA TASTY</b><b>MEGA SLIM</b><span>CONDOMS</span></div>
    <div class="pack__rule pack__rule--lower"></div>
    <h2 class="pack__claim">SAFE<br>SEX<br>GREAT<br>SEX</h2>
    <div class="pack__fruit" role="img" aria-label="Photo of a pile of fresh strawberries"></div>
    <p class="pack__flavour">STRAWBERRY FLAVORED</p>
    <p class="pack__code">53</p>
  </article>

  <article class="pack pack--orange">
    <div class="pack__top-band"></div>
    <div class="pack__ribbons" role="img" aria-label="Translucent orange smoke ribbons"></div>
    <div class="pack__brand"><span class="pack__brand-dot"></span>VORO</div>
    <div class="pack__count">12</div>
    <div class="pack__rule pack__rule--upper"></div>
    <div class="pack__variant"><b>MEGA TASTY</b><b>MEGA SLIM</b><span>CONDOMS</span></div>
    <div class="pack__rule pack__rule--lower"></div>
    <h2 class="pack__claim">SAFE<br>SEX<br>GREAT<br>SEX</h2>
    <div class="pack__fruit" role="img" aria-label="Photo of a whole orange with sliced halves and leaves"></div>
    <p class="pack__flavour">ORANGE FLAVORED</p>
    <p class="pack__code">53</p>
  </article>
</main>
</body>
</html>
```